Project Manager Business Card for Top Architectural Firm

Update and design a stunning Senior Project Manager Business Card

MARCO T. RUEDA II
Senior Project Manager

H A R B O R L I N E
A R C H I T E C T U R E L L C.
www.HarborlineCrestHouses.com
4217 NW 38th Ter. Suite 905
Miami, FL 33172
C: (305) 418-2273
mrueda.harborlinecresthouses@mailvista.net

Looking to have the logo to be UV Spot ink printed and to be prominent.

Target Market(s)

High end real estate architecture construction

Industry/Entity Type

Architect

Contact Information for Business Card

MARCO T. RUEDA II
Senior Project Manager

H A R B O R L I N E
Miami, FL 33172
C: (305) 418-2273

Font styles to use
Sans Serif

Colors

Designer to choose colors to be used in the design.

Requirements
Must have
• Prominent Logo

```html
<!DOCTYPE html>
<html lang="en">
<head>
<meta charset="utf-8">
<title>Harborline Architecture – Business Card</title>
<link href="https://fonts.googleapis.com/css2?family=Montserrat:wght@300;400;600&family=Open+Sans:wght@600&display=swap" rel="stylesheet">
<style>
  :root {
    --backdrop: #141414;
    --card-base: #1b1c1f;
    --photo-warm: #2d2822;
    --photo-deep: #191714;
    --silver: #c9cbcf;
    --silver-soft: #a9acb1;
    --accent: #3fa9c9;
  }
  html, body {
    margin: 0;
    width: 1200px;
    height: 900px;
    overflow: hidden;
    background: var(--backdrop);
  }
  .canvas {
    position: relative;
    width: 1200px;
    height: 900px;
  }
  .card {
    position: absolute;
    left: 75px;
    top: 150px;
    width: 1050px;
    height: 600px;
    border-radius: 30px;
    background: var(--card-base);
    overflow: hidden;
    box-shadow: 0 20px 50px rgba(0,0,0,.6);
  }
  .card__photo {
    position: absolute;
    left: 0;
    top: 110px;
    width: 100%;
    height: 490px;
    background: linear-gradient(180deg, var(--photo-warm) 0%, var(--photo-deep) 100%);
    opacity: .85;
  }
  .brand {
    position: absolute;
    left: 70px;
    top: 150px;
    color: var(--silver);
    font-family: "Montserrat", sans-serif;
    font-weight: 300;
  }
  .brand__row {
    display: flex;
    align-items: center;
    gap: 22px;
  }
  .brand__dot {
    width: 64px;
    height: 64px;
    border-radius: 50%;
    background: var(--accent);
    flex: none;
  }
  .brand__name {
    font-size: 50px;
    letter-spacing: 8px;
    line-height: 1;
  }
  .brand__sub {
    margin: 18px 0 0 86px;
    font-size: 17px;
    letter-spacing: 7px;
  }
  .contact {
    position: absolute;
    left: 560px;
    top: 250px;
    color: var(--silver);
  }
  .contact__name {
    margin: 0;
    font-family: "Montserrat", sans-serif;
    font-weight: 600;
    font-size: 36px;
    letter-spacing: 1px;
  }
  .contact__title {
    margin: 4px 0 22px;
    font-family: "Montserrat", sans-serif;
    font-weight: 300;
    font-size: 21px;
    color: var(--silver-soft);
  }
  .contact__list {
    list-style: none;
    margin: 0;
    padding: 0;
    font-family: "Open Sans", sans-serif;
    font-weight: 600;
    font-size: 18px;
    line-height: 1.35;
  }
  .contact__item {
    display: flex;
    align-items: flex-start;
    gap: 14px;
    margin-bottom: 10px;
  }
  .contact__icon {
    width: 24px;
    height: 24px;
    flex: none;
  }
</style>
</head>
<body>
<div class="canvas">
  <section class="card">
    <div class="card__photo" role="img" aria-label="Dimmed photograph of a modern luxury home facade"></div>

    <div class="brand">
      <div class="brand__row">
        <span class="brand__dot"></span>
        <span class="brand__name">HARBORLINE</span>
      </div>
      <div class="brand__sub">ARCHITECTURE LLC.</div>
    </div>

    <div class="contact">
      <h1 class="contact__name">MARCO T. RUEDA II</h1>
      <p class="contact__title">Senior Project Manager</p>
      <ul class="contact__list">
        <li class="contact__item">
          <svg class="contact__icon" viewBox="0 0 24 24" fill="none" stroke="#c9cbcf" stroke-width="1.6"><circle cx="12" cy="12" r="11"/><path d="M12 18s-4-4.2-4-7a4 4 0 0 1 8 0c0 2.8-4 7-4 7z"/><circle cx="12" cy="11" r="1.4"/></svg>
          <span>4217 NW 38th Ter. Suite 905<br>Miami, FL 33172</span>
        </li>
        <li class="contact__item">
          <svg class="contact__icon" viewBox="0 0 24 24" fill="none" stroke="#c9cbcf" stroke-width="1.6"><circle cx="12" cy="12" r="11"/><path d="M8.5 7.5l2 2-1.2 1.5a7 7 0 0 0 3.7 3.7l1.5-1.2 2 2-1.3 1.5c-4 0-8-4-8-8z"/></svg>
          <span>(305) 418-2273</span>
        </li>
        <li class="contact__item">
          <svg class="contact__icon" viewBox="0 0 24 24" fill="none" stroke="#c9cbcf" stroke-width="1.6"><circle cx="12" cy="12" r="11"/><rect x="6.5" y="8" width="11" height="8" rx="1"/><path d="M6.5 8.5l5.5 4 5.5-4"/></svg>
          <span>mrueda.harborlinecresthouses@mailvista.net</span>
        </li>
        <li class="contact__item">
          <svg class="contact__icon" viewBox="0 0 24 24" fill="none" stroke="#c9cbcf" stroke-width="1.6"><circle cx="12" cy="12" r="11"/><circle cx="12" cy="12" r="6"/><path d="M6 12h12M12 6c-2.2 2.5-2.2 9.5 0 12M12 6c2.2 2.5 2.2 9.5 0 12"/></svg>
          <span>www.HarborlineCrestHouses.com</span>
        </li>
      </ul>
    </div>
  </section>
</div>
</body>
</html>
```